its a towing company , its called kwm towing and transport. kwm stands for kept with merit. on the card looking for colors mainly red with gray and black and white. what the company do. local and long distances ,buy junk cars , snow plow available .tire change ,jumpstart ,and fuel delivery find us on pagewell . kwmtowing@mailora.com. fax no#555-210-4867 phone no#555-386-2074

something that defines kept with merit

Decorative

ef444b
1b1b1b
9d9d9d
ffffff

• pics of chains or flatbed varn in red
• no cartoons

```html
<!DOCTYPE html>
<html lang="en">
<head>
<meta charset="utf-8">
<title>kwm towing and transport – business card</title>
<link rel="stylesheet" href="https://fonts.googleapis.com/css2?family=Saira+Semi+Condensed:wght@600;700;800&family=Roboto:wght@400;500;700&display=swap">
<style>
  :root {
    --page: #dcdddf;
    --card-dark: #231f20;
    --photo-gray: #3a3a3c;
    --red: #d41c2f;
    --red-deep: #9c1420;
    --gray: #9d9d9d;
    --rule: #8a8a8a;
    --white: #ffffff;
  }
  * { box-sizing: border-box; margin: 0; padding: 0; }
  html, body { width: 1200px; height: 471px; overflow: hidden; }
  body { background: var(--page); position: relative; font-family: "Roboto", sans-serif; }

  .card {
    position: absolute; top: 86px; width: 526px; height: 299px;
    background: var(--card-dark); overflow: hidden;
    box-shadow: 0 2px 6px rgba(0,0,0,.25);
  }
  .card--front { left: 52px; }
  .card--back { left: 622px; }

  .front__photo {
    position: absolute; inset: 0;
    background:
      linear-gradient(90deg, var(--red) 0%, var(--red-deep) 22%, #1e1e1e 34%, #5a5a5a 46%, #2a2a2a 58%, var(--photo-gray) 72%, #454547 100%);
  }

  .services {
    position: absolute; right: 20px; top: 67px;
    list-style: none;
    font-family: "Saira Semi Condensed", sans-serif; font-weight: 700;
    font-size: 19px; color: var(--white); line-height: 27.5px;
  }
  .services li { display: flex; justify-content: flex-end; align-items: center; gap: 9px; }
  .services svg { width: 20px; height: 20px; flex: none; }

  .payment-note {
    position: absolute; right: 23px; top: 268px;
    font-family: "Roboto", sans-serif; font-weight: 700; font-size: 11.5px;
    letter-spacing: 0.9px; color: var(--white);
  }

  .brand {
    position: absolute; right: 24px; top: 10px; text-align: right;
    font-family: "Saira Semi Condensed", sans-serif; font-weight: 800; color: var(--red);
  }
  .brand__name { font-size: 132px; line-height: 118px; letter-spacing: -3px; }
  .brand__tagline { font-size: 22px; line-height: 24px; text-transform: uppercase; letter-spacing: 0.3px; }

  .holder {
    position: absolute; left: 23px; top: 181px;
    font-family: "Saira Semi Condensed", sans-serif; font-weight: 700;
    font-size: 25px; color: var(--white);
  }
  .divider { position: absolute; left: 23px; right: 23px; top: 221px; height: 2px; background: var(--rule); }

  .contact {
    position: absolute; top: 240px; list-style: none;
    font-size: 14px; letter-spacing: 1.1px; color: var(--white); line-height: 21px;
  }
  .contact li { display: flex; align-items: center; gap: 8px; }
  .contact--phones { left: 23px; }
  .contact--online { right: 23px; }
  .contact--online li { justify-content: flex-end; }
  .contact svg { width: 13px; height: 13px; flex: none; fill: var(--red); }
</style>
</head>
<body>

<section class="card card--front">
  <div class="front__photo" role="img" aria-label="Photo of a red car's rear wheel fitted with snow chains"></div>
  <ul class="services">
    <li>Local &amp; Long Distances <svg viewBox="0 0 20 20"><rect x="1.5" y="2.5" width="15" height="15" rx="3" fill="none" stroke="#fff" stroke-width="2.2"/><path d="M5 10l4 4 9-10" fill="none" stroke="#fff" stroke-width="3" stroke-linecap="round" stroke-linejoin="round"/></svg></li>
    <li>Buy Junk Cars <svg viewBox="0 0 20 20"><rect x="1.5" y="2.5" width="15" height="15" rx="3" fill="none" stroke="#fff" stroke-width="2.2"/><path d="M5 10l4 4 9-10" fill="none" stroke="#fff" stroke-width="3" stroke-linecap="round" stroke-linejoin="round"/></svg></li>
    <li>Snow Plow Available <svg viewBox="0 0 20 20"><rect x="1.5" y="2.5" width="15" height="15" rx="3" fill="none" stroke="#fff" stroke-width="2.2"/><path d="M5 10l4 4 9-10" fill="none" stroke="#fff" stroke-width="3" stroke-linecap="round" stroke-linejoin="round"/></svg></li>
    <li>Tire Change <svg viewBox="0 0 20 20"><rect x="1.5" y="2.5" width="15" height="15" rx="3" fill="none" stroke="#fff" stroke-width="2.2"/><path d="M5 10l4 4 9-10" fill="none" stroke="#fff" stroke-width="3" stroke-linecap="round" stroke-linejoin="round"/></svg></li>
    <li>Jumpstart <svg viewBox="0 0 20 20"><rect x="1.5" y="2.5" width="15" height="15" rx="3" fill="none" stroke="#fff" stroke-width="2.2"/><path d="M5 10l4 4 9-10" fill="none" stroke="#fff" stroke-width="3" stroke-linecap="round" stroke-linejoin="round"/></svg></li>
    <li>Fuel Delivery <svg viewBox="0 0 20 20"><rect x="1.5" y="2.5" width="15" height="15" rx="3" fill="none" stroke="#fff" stroke-width="2.2"/><path d="M5 10l4 4 9-10" fill="none" stroke="#fff" stroke-width="3" stroke-linecap="round" stroke-linejoin="round"/></svg></li>
  </ul>
  <p class="payment-note">CREDIT CARD ACCEPTED</p>
</section>

<section class="card card--back">
  <div class="brand">
    <div class="brand__name">kwm</div>
    <div class="brand__tagline">towing &amp; transport</div>
  </div>

  <h1 class="holder">John Doe</h1>
  <div class="divider"></div>

  <ul class="contact contact--phones">
    <li><svg viewBox="0 0 24 24"><path d="M6.6 10.8a15.1 15.1 0 0 0 6.6 6.6l2.2-2.2c.3-.3.7-.4 1-.2 1.1.4 2.3.6 3.6.6.6 0 1 .4 1 1V20c0 .6-.4 1-1 1C10.6 21 3 13.4 3 4c0-.6.4-1 1-1h3.5c.6 0 1 .4 1 1 0 1.3.2 2.5.6 3.6.1.3 0 .7-.2 1z"/></svg>555-386-2074</li>
    <li><svg viewBox="0 0 24 24"><path d="M6 2h12v6H6z"/><path d="M3 9h18a1 1 0 0 1 1 1v7h-4v5H6v-5H2v-7a1 1 0 0 1 1-1zm5 7v4h8v-4z"/></svg>555-210-4867</li>
  </ul>

  <ul class="contact contact--online">
    <li>kwmtowing@mailora.com <svg viewBox="0 0 24 24"><path d="M2 5h20v14H2z"/><path d="M2 5l10 8 10-8" fill="none" stroke="#231f20" stroke-width="2"/></svg></li>
    <li>pagewell.com/kwmtowing <svg viewBox="0 0 24 24"><rect x="5" y="3" width="14" height="18"/></svg></li>
  </ul>
</section>

</body>
</html>
```